Bref créative
Stationary Package - Paper, Envelope, Fax Cover, Bus. Card
Mortgage Co. seeks Stationary Package
Professional
Marla Henson
Broker / Owner
246 W. "K" Avenue
Upland CA 91704
MarlaHenson@quillmail.example
DRE LIC 05837162 NMLS 489153
Head Shot Photo on Front about a 1/3 of the card to 1/4. Should have company name/logo on the front "KGV Lending Corp." or Corporation whichever looks better
MarlaHenson.example MarlaHensonRE.example KGVLending.example
Home Loans & Real Estate Investments,
Mortgage Broker, Licensed Real Estate Broker,
California Certified Residential Property Manager (CPM),
Short Sale & Foreclosure Resource Certified (SFR),
BS Business Admin., University of Brookhollow, CA

```html
<!DOCTYPE html>
<html lang="en">
<head>
<meta charset="utf-8">
<title>KGV Mortgage &amp; Real Estate — Stationery</title>
<link href="https://fonts.googleapis.com/css2?family=Open+Sans:wght@400;600;700&display=swap" rel="stylesheet">
<style>
  :root {
    --canvas: #ffffff;
    --paper: #ffffff;
    --ink: #2b2b2b;
    --ink-soft: #555555;
    --accent-blue: #1f6fc0;
    --deep-blue: #123f7a;
    --charcoal: #1c1c1c;
    --graphite: #4a4a4a;
    --orange: #f08a1c;
    --faint: #ececec;
  }
  * { margin: 0; padding: 0; box-sizing: border-box; }
  html, body { width: 1200px; height: 715px; overflow: hidden; background: var(--canvas); }
  body { position: relative; font-family: "Open Sans", Arial, sans-serif; color: var(--ink); }

  .letterhead {
    position: absolute; left: 12px; top: 10px; width: 574px; height: 698px;
    background: var(--paper); box-shadow: 0 0 3px rgba(0,0,0,.35); overflow: hidden;
  }
  .brand { position: absolute; display: flex; align-items: center; gap: 8px; }
  .brand-dot { width: 30px; height: 30px; border-radius: 50%; background: var(--orange); flex: none; }
  .brand-name {
    font-family: "Open Sans", Arial, sans-serif; font-weight: 600; color: var(--ink);
    line-height: 1.02; letter-spacing: .5px;
  }
  .letterhead .brand { left: 24px; top: 30px; }
  .letterhead .brand-name { font-size: 19px; }
  .address { position: absolute; left: 26px; top: 96px; font-size: 12.5px; color: var(--ink); }
  .signer { position: absolute; left: 422px; top: 92px; }
  .signer-name { font-size: 15px; font-weight: 700; color: var(--accent-blue); }
  .signer-title { font-size: 11px; color: var(--ink-soft); }

  .faint-mark {
    position: absolute; left: 150px; top: 500px;
    font-size: 86px; font-weight: 600; color: var(--faint); letter-spacing: 4px;
  }

  .wave { position: absolute; left: 0; display: block; }
  .letterhead .wave { bottom: 0; width: 574px; height: 130px; }

  .contact { position: absolute; display: grid; grid-template-columns: auto auto; column-gap: 10px; row-gap: 1px; font-size: 9.5px; line-height: 1.35; }
  .contact dt { font-weight: 700; text-align: right; }
  .letterhead .contact { left: 232px; top: 634px; color: #ffffff; }
  .letterhead .contact dd { color: #d7d7d7; }

  .envelope {
    position: absolute; left: 600px; top: 168px; width: 588px; height: 444px;
    background: linear-gradient(180deg, #ffffff 0%, #f4f4f4 55%, #dcdcdc 100%);
    box-shadow: 0 0 3px rgba(0,0,0,.35); overflow: hidden;
  }
  .envelope-flap { position: absolute; left: 0; top: 0; width: 100%; height: 44px; background: linear-gradient(180deg, #111 0%, #2e2e2e 100%); }
  .envelope .brand { left: 14px; top: 72px; }
  .envelope .brand-name { font-size: 20px; }
  .envelope .contact { left: 228px; top: 216px; color: var(--ink); }
  .envelope .contact dd { color: var(--ink-soft); }
  .envelope .wave { bottom: 0; width: 588px; height: 150px; }
</style>
</head>
<body>

<section class="letterhead" aria-label="Letterhead">
  <div class="brand">
    <span class="brand-dot"></span>
    <span class="brand-name">KGV Mortgage &amp;<br>Real Estate</span>
  </div>
  <p class="address">246 W. "K" Avenue, Upland CA 91704</p>
  <div class="signer">
    <p class="signer-name">Marla Henson</p>
    <p class="signer-title">Broker / Owner</p>
  </div>
  <div class="faint-mark">KGV</div>

  <svg class="wave" viewBox="0 0 574 130" preserveAspectRatio="none" aria-hidden="true">
    <defs>
      <linearGradient id="lhDark" x1="0" y1="0" x2="0" y2="1">
        <stop offset="0" stop-color="#4a4a4a"/>
        <stop offset="1" stop-color="#141414"/>
      </linearGradient>
    </defs>
    <path d="M0 112 C150 60 380 30 574 38 L574 130 L0 130 Z" fill="url(#lhDark)"/>
    <path d="M0 104 C150 52 380 20 574 26 L574 38 C380 32 150 62 0 114 Z" fill="var(--accent-blue)"/>
    <path d="M0 114 C150 62 380 32 574 38 L574 42 C380 38 150 68 0 118 Z" fill="var(--deep-blue)"/>
  </svg>
  <dl class="contact">
    <dt>Phone</dt><dd>909-555-0142</dd>
    <dt>Cell</dt><dd>909-555-0187</dd>
    <dt>Fax</dt><dd>909-555-0163</dd>
    <dt>Email</dt><dd>MarlaHenson@quillmail.example</dd>
  </dl>
</section>

<section class="envelope" aria-label="Envelope">
  <div class="envelope-flap"></div>
  <div class="brand">
    <span class="brand-dot"></span>
    <span class="brand-name">KGV Mortgage &amp;<br>Real Estate</span>
  </div>
  <dl class="contact">
    <dt>Phone</dt><dd>909-555-0142</dd>
    <dt>Cell</dt><dd>909-555-0187</dd>
    <dt>Fax</dt><dd>909-555-0163</dd>
    <dt>Email</dt><dd>MarlaHenson@quillmail.example</dd>
  </dl>
  <svg class="wave" viewBox="0 0 588 150" preserveAspectRatio="none" aria-hidden="true">
    <defs>
      <linearGradient id="envDark" x1="0" y1="0" x2="0" y2="1">
        <stop offset="0" stop-color="#3c3c3c"/>
        <stop offset="1" stop-color="#0e0e0e"/>
      </linearGradient>
    </defs>
    <path d="M0 84 C180 58 400 56 588 72 L588 150 L0 150 Z" fill="url(#envDark)"/>
    <path d="M0 76 C180 48 400 44 588 60 L588 72 C400 58 180 60 0 86 Z" fill="var(--accent-blue)"/>
    <path d="M0 86 C180 60 400 58 588 72 L588 76 C400 64 180 66 0 90 Z" fill="var(--deep-blue)"/>
  </svg>
</section>

</body>
</html>
```